PowerPoint template for large technology company

Requesting proposals for a PowerPoint deck template that can be used by our sales team when pitching clients. We are a large technology media company, that is BtoB focused, and are looking for a professional, clean, tech-forward, design and layout. However, our clients are advertisers and brands who would respond well to a subtly stylized creative design.

We need a fully built-out template wherein our sales team can choose from a variety of slide layouts while compiling their pitch decks.

Key objective: To create a template that mandates consistent fonts, sizes, and layout, and is easy to use for novice presenters. A plug-and-play template.

Secondary objective: A refresh on current design of company template.

Presentation template should include:
2 Presentation title slide options
2 Section header options
6 information layout slide options
3 data charts (pie, bar, and column)
Summary/ Thank you slide

The teams using this template will not be adept with PowerPoint but should easily be able to insert images and text boxes without it ruining the design and format of the presentation. The idea is if 20 people use our template to build pitch-decks, all of the individual decks should all look like they came from the same team. Please be as detailed and specific as possible when building out slides.

Simple, high-compatibility fonts. Please see brand guidelines attached.

Target Market(s)

Large advertising agencies and major consumer technology brands.

This deck template will not be consumer facing.

Industry/Entity Type

Building

Font styles to use
Serif
Sans Serif

Requirements
Must have
• Must be clean, high-tech, and forces user to stay within template guidelines during modifications.

Template should be built out for a sales presentation that will be a tool for ppt novices.
Nice to have
• As we are revamping existing decks, it will be nice to see multiple ideas on the design. Think professional, high-tech, and powerful.
Should not have
• Should not have a distracting background that will interfere with presentations or where it will be difficult to easily insert images.

Blacked out backgrounds cause a "boxed in" look for images and/or text boxes - which is undesirable. Either don't include color-blocked backgrounds or introduce a way in which this can be used that avoids the previously stated pitfall.

No rotated text-fill options. (i.e. rotating text by 90 or 180 degrees)

Please don't be too literal in your design approach.

```html
<!DOCTYPE html>
<html lang="en">
<head>
<meta charset="utf-8">
<title>NodeHarbor Sales Deck Template</title>
<link rel="stylesheet" href="https://fonts.googleapis.com/css2?family=Roboto+Condensed:wght@400;500;700&display=swap">
<style>
  :root {
    --brand-blue: #0b6fa6;
    --ink-dark: #333b43;
    --slate-grey: #7c8891;
    --paper: #ffffff;
    --frame: #6a6a6a;
    --rule: #c9ced2;
    --grid: #d5d9dc;
    --body-ink: #2a2a2a;
  }
  * { box-sizing: border-box; margin: 0; padding: 0; }
  html, body {
    width: 1200px; height: 1000px; overflow: hidden;
    background: var(--paper);
    font-family: "Roboto Condensed", "Arial Narrow", sans-serif;
    color: var(--body-ink);
  }
  .canvas { position: relative; width: 1200px; height: 1000px; }

  .slide { position: absolute; width: 551px; height: 310px; overflow: hidden; }
  .slide--light { background: var(--paper); border: 1px solid var(--frame); }
  .slide--brand { background: var(--brand-blue); color: var(--paper); }
  .slide > * { position: absolute; }

  .pos-a { left: 39px; top: 22px; }
  .pos-b { left: 612px; top: 22px; }
  .pos-c { left: 39px; top: 343px; }
  .pos-d { left: 612px; top: 343px; }
  .pos-e { left: 39px; top: 665px; }
  .pos-f { left: 612px; top: 665px; }

  /* title slide */
  .cover-title { left: 57px; top: 143px; font-size: 15px; font-weight: 400; letter-spacing: .3px; }
  .cover-title b, .slide-title b { font-weight: 700; }
  .cover-presenter { left: 57px; top: 170px; font-size: 9.5px; font-weight: 700; line-height: 12px; }
  .cover-network { left: 170px; top: 70px; width: 365px; height: 200px;
    background: radial-gradient(ellipse at 55% 45%, rgba(255,255,255,.18), rgba(255,255,255,0) 70%); }
  .cover-brand { left: 58px; top: 255px; font-size: 19px; font-weight: 400; color: var(--paper); }

  /* header tag */
  .slide-tag { top: 20px; right: 22px; display: flex; align-items: center; gap: 5px; position: absolute; }
  .slide-tag__label { font-size: 7.5px; font-weight: 700; color: var(--body-ink); }
  .slide-tag__num { width: 12px; height: 11px; background: var(--slate-grey); color: var(--paper);
    font-size: 7px; display: flex; align-items: center; justify-content: center; }
  .slide-tag__rule { width: 1px; height: 14px; background: var(--body-ink); margin: 0 2px; }
  .slide-tag__brand { font-size: 11px; color: var(--brand-blue); font-weight: 400; }

  .slide-title { left: 50px; top: 28px; font-size: 25px; font-weight: 400; color: var(--brand-blue); letter-spacing: .2px; }
  .slide-title--about { left: 54px; top: 35px; }
  .slide-intro { left: 52px; top: 70px; width: 470px; font-size: 9.3px; font-weight: 500; line-height: 12px; color: var(--body-ink); }

  /* about */
  .about-visual { left: 51px; top: 79px; width: 177px; height: 169px;
    background: radial-gradient(circle at 55% 40%, #2a8fcb, #0b6fa6 60%, #085a88); }
  .about-lead { left: 259px; top: 78px; width: 240px; font-size: 10px; font-weight: 500; line-height: 12px; color: var(--body-ink); }
  .about-body { left: 259px; top: 126px; width: 240px; font-size: 6.6px; line-height: 9.3px; color: var(--body-ink); }
  .about-body p + p { margin-top: 9px; }

  /* nav */
  .slide-nav { right: 12px; bottom: 10px; width: 31px; height: 15px; }

  /* charts */
  .bar-chart { width: 200px; height: 100px; }
  .chart-legend { width: 40px; }
  .legend-item { display: flex; flex-direction: column; align-items: center; font-size: 6.5px; font-weight: 500; color: var(--ink-dark); margin-bottom: 18px; }
  .legend-dot { width: 12px; height: 12px; border-radius: 50%; margin-bottom: 4px; }
  .legend-dot--tablet { background: var(--brand-blue); }
  .legend-dot--laptop { background: var(--ink-dark); }
  .bar-caption { width: 58px; }
  .caption-heading { font-size: 7.5px; font-weight: 500; color: var(--brand-blue); white-space: nowrap; }
  .caption-body { font-size: 5.3px; line-height: 6.4px; margin-top: 3px; color: var(--body-ink); }

  .slide-divider { left: 0; top: 254px; width: 100%; height: 1px; background: var(--rule); }
  .slide-footnote { left: 52px; top: 257px; width: 470px; font-size: 6.8px; line-height: 10px; color: var(--body-ink); }

  /* pie */
  .donut { width: 120px; height: 120px; }
  .pie-callout { width: 80px; }
  .pie-value { font-size: 17px; font-weight: 700; color: var(--brand-blue); line-height: 18px; }
  .pie-heading { font-size: 8px; font-weight: 500; color: var(--brand-blue); margin-top: 1px; }
  .pie-body { font-size: 5.5px; line-height: 6.6px; width: 50px; margin-top: 2px; }
  .callout-lines { left: 0; top: 0; width: 551px; height: 250px; }

  /* options */
  .option-card { width: 110px; }
  .option-visual { width: 95px; height: 98px; }
  .option-visual--grey { background: var(--slate-grey); }
  .option-visual--blue { background: var(--brand-blue); }
  .option-visual--dark { background: var(--ink-dark); }
  .option-heading { font-size: 8.5px; font-weight: 500; color: var(--brand-blue); margin-top: 4px; }
  .option-body { font-size: 5.6px; line-height: 6.9px; width: 100px; margin-top: 4px; }

  /* closing */
  .closing-bubbles { left: 170px; top: 50px; width: 245px; height: 165px; }
  .closing-rule { top: 253px; height: 1px; background: rgba(255,255,255,.8); }
  .closing-rule--left { left: 0; width: 212px; }
  .closing-rule--right { left: 343px; width: 208px; }
  .closing-title { left: 212px; width: 131px; top: 243px; text-align: center; font-size: 16px; font-weight: 700; }
  .closing-note { left: 212px; width: 131px; top: 265px; text-align: center; font-size: 5.5px; line-height: 6.5px; font-weight: 500; }
</style>
</head>
<body>
<main class="canvas">

  <!-- Title slide -->
  <section class="slide slide--brand pos-a">
    <div class="cover-network" role="img" aria-label="Faint network of connected nodes and lines"></div>
    <h1 class="cover-title">DATA DRIVE <b>PERFORMANCE</b></h1>
    <p class="cover-presenter">Presented by: Daniel Morrow<br>President, CEO, NodeHarbor</p>
    <div class="cover-brand">NodeHarbor</div>
  </section>

  <!-- About us -->
  <section class="slide slide--light pos-b">
    <div class="slide-tag"><span class="slide-tag__label">About Us</span><span class="slide-tag__num">01</span><span class="slide-tag__rule"></span><span class="slide-tag__brand">NodeHarbor</span></div>
    <h2 class="slide-title slide-title--about">ABOUT <b>US</b></h2>
    <div class="about-visual" role="img" aria-label="Blue image of a connected node network"></div>
    <p class="about-lead">This is an example to be replace with own text here, or what you want to put a here instead this dummy text Dont forget to remove this once you put your own text.</p>
    <div class="about-body">
      <p>This is an example to be replace with own text here, or what you want to put a here instead this dummy text. Dont forget to remove this once you put your own text. This is an example to be replace with own text here, or what you want to put a here instead this dummy text. Dont forget to remove this once you put your own text. This is an example to be replace with own text here, or what you want to put a here instead this dummy text. Dont forget to remove this once you put your own text.</p>
      <p>This is an example to be replace with own text here, or what you want to put a here instead this dummy text. Dont forget to remove this once you put your own text. This is an example to be replace with own text here, or what you want to put a here instead this dummy text.</p>
    </div>
    <svg class="slide-nav" viewBox="0 0 31 15" aria-label="Previous and next"><circle cx="7.5" cy="7.5" r="7.5" fill="#0b6fa6"/><path d="M9 4 L5.5 7.5 L9 11" stroke="#fff" stroke-width="2" fill="none"/><circle cx="23.5" cy="7.5" r="7.5" fill="#0b6fa6"/><path d="M22 4 L25.5 7.5 L22 11" stroke="#fff" stroke-width="2" fill="none"/></svg>
  </section>

  <!-- Bar charts -->
  <section class="slide slide--light pos-c">
    <div class="slide-tag"><span class="slide-tag__label">Bar</span><span class="slide-tag__num">02</span><span class="slide-tag__rule"></span><span class="slide-tag__brand">NodeHarbor</span></div>
    <h2 class="slide-title">DATA <b>CHARTS:</b> Bar</h2>
    <p class="slide-intro">This is an example to be replace with own text here, or what you want to put a here instead this dummy text Dont forget to remove this once you put your own text.</p>

    <svg class="bar-chart" style="left:45px;top:110px" viewBox="0 0 200 100" aria-label="Bar chart comparing tablet and laptop">
      <g stroke="#d5d9dc" stroke-width=".6"><line x1="12" x2="185" y1="82.6" y2="82.6"/><line x1="12" x2="185" y1="73.1" y2="73.1"/><line x1="12" x2="185" y1="63.7" y2="63.7"/><line x1="12" x2="185" y1="54.2" y2="54.2"/><line x1="12" x2="185" y1="44.8" y2="44.8"/><line x1="12" x2="185" y1="35.4" y2="35.4"/><line x1="12" x2="185" y1="25.9" y2="25.9"/><line x1="12" x2="185" y1="16.5" y2="16.5"/><line x1="12" x2="185" y1="7" y2="7"/></g>
      <g font-size="6" fill="#0b6fa6" font-family="Roboto Condensed, sans-serif" text-anchor="middle"><text x="5" y="94">0</text><text x="5" y="84.6">1</text><text x="5" y="75.1">2</text><text x="5" y="65.7">3</text><text x="5" y="56.2">4</text><text x="5" y="46.8">5</text><text x="5" y="37.4">6</text><text x="5" y="27.9">7</text><text x="5" y="18.5">8</text><text x="5" y="9">9</text></g>
      <line x1="12" x2="12" y1="5" y2="92" stroke="#0b6fa6" stroke-width="1"/>
      <line x1="12" x2="185" y1="92" y2="92" stroke="#0b6fa6" stroke-width="1"/>
      <rect x="28" y="45" width="18" height="47" fill="#333b43"/><rect x="47" y="16.5" width="19" height="75.5" fill="#0b6fa6"/>
      <rect x="84" y="54" width="18" height="38" fill="#333b43"/><rect x="103" y="16.5" width="19" height="75.5" fill="#0b6fa6"/>
      <rect x="140" y="45" width="18" height="47" fill="#333b43"/><rect x="159" y="16.5" width="19" height="75.5" fill="#0b6fa6"/>
      <g font-size="7" font-weight="500" fill="#333b43" font-family="Roboto Condensed, sans-serif" text-anchor="middle"><text x="37" y="41">40%</text><text x="56.5" y="13">60%</text><text x="93" y="50">30%</text><text x="112.5" y="13">70%</text><text x="149" y="41">40%</text><text x="168.5" y="13">60%</text></g>
    </svg>
    <div class="chart-legend" style="left:230px;top:116px"><div class="legend-item"><span class="legend-dot legend-dot--tablet"></span>Tablet</div><div class="legend-item"><span class="legend-dot legend-dot--laptop"></span>Laptop</div></div>
    <div class="bar-caption" style="left:68px;top:209px"><div class="caption-heading">Sample Heading 1</div><p class="caption-body">This is an example to be replace with own text here</p></div>
    <div class="bar-caption" style="left:123px;top:209px"><div class="caption-heading">Sample Heading 1</div><p class="caption-body">This is an example to be replace with own text here</p></div>
    <div class="bar-caption" style="left:180px;top:209px"><div class="caption-heading">Sample Heading 1</div><p class="caption-body">This is an example to be replace with own text here</p></div>

    <svg class="bar-chart" style="left:286px;top:110px" viewBox="0 0 200 100" aria-label="Bar chart comparing tablet and laptop">
      <g stroke="#d5d9dc" stroke-width=".6"><line x1="12" x2="185" y1="82.6" y2="82.6"/><line x1="12" x2="185" y1="73.1" y2="73.1"/><line x1="12" x2="185" y1="63.7" y2="63.7"/><line x1="12" x2="185" y1="54.2" y2="54.2"/><line x1="12" x2="185" y1="44.8" y2="44.8"/><line x1="12" x2="185" y1="35.4" y2="35.4"/><line x1="12" x2="185" y1="25.9" y2="25.9"/><line x1="12" x2="185" y1="16.5" y2="16.5"/><line x1="12" x2="185" y1="7" y2="7"/></g>
      <g font-size="6" fill="#0b6fa6" font-family="Roboto Condensed, sans-serif" text-anchor="middle"><text x="5" y="94">0</text><text x="5" y="84.6">1</text><text x="5" y="75.1">2</text><text x="5" y="65.7">3</text><text x="5" y="56.2">4</text><text x="5" y="46.8">5</text><text x="5" y="37.4">6</text><text x="5" y="27.9">7</text><text x="5" y="18.5">8</text><text x="5" y="9">9</text></g>
      <line x1="12" x2="12" y1="5" y2="92" stroke="#0b6fa6" stroke-width="1"/>
      <line x1="12" x2="185" y1="92" y2="92" stroke="#0b6fa6" stroke-width="1"/>
      <rect x="28" y="45" width="18" height="47" fill="#333b43"/><rect x="47" y="16.5" width="19" height="75.5" fill="#0b6fa6"/>
      <rect x="84" y="54" width="18" height="38" fill="#333b43"/><rect x="103" y="16.5" width="19" height="75.5" fill="#0b6fa6"/>
      <rect x="140" y="45" width="18" height="47" fill="#333b43"/><rect x="159" y="16.5" width="19" height="75.5" fill="#0b6fa6"/>
      <g font-size="7" font-weight="500" fill="#333b43" font-family="Roboto Condensed, sans-serif" text-anchor="middle"><text x="37" y="41">40%</text><text x="56.5" y="13">60%</text><text x="93" y="50">30%</text><text x="112.5" y="13">70%</text><text x="149" y="41">40%</text><text x="168.5" y="13">60%</text></g>
    </svg>
    <div class="chart-legend" style="left:471px;top:116px"><div class="legend-item"><span class="legend-dot legend-dot--tablet"></span>Tablet</div><div class="legend-item"><span class="legend-dot legend-dot--laptop"></span>Laptop</div></div>
    <div class="bar-caption" style="left:308px;top:209px"><div class="caption-heading">Sample Heading 1</div><p class="caption-body">This is an example to be replace with own text here</p></div>
    <div class="bar-caption" style="left:364px;top:209px"><div class="caption-heading">Sample Heading 1</div><p class="caption-body">This is an example to be replace with own text here</p></div>
    <div class="bar-caption" style="left:422px;top:209px"><div class="caption-heading">Sample Heading 1</div><p class="caption-body">This is an example to be replace with own text here</p></div>

    <div class="slide-divider"></div>
    <p class="slide-footnote">This is an example to be replace with own text here, or what you want to put a here instead this dummy text. Dont forget to remove this once you put your own text.<br>This is an example to be replace with own text here, or what you want to put a here instead this dummy text.</p>
    <svg class="slide-nav" viewBox="0 0 31 15" aria-label="Previous and next"><circle cx="7.5" cy="7.5" r="7.5" fill="#0b6fa6"/><path d="M9 4 L5.5 7.5 L9 11" stroke="#fff" stroke-width="2" fill="none"/><circle cx="23.5" cy="7.5" r="7.5" fill="#0b6fa6"/><path d="M22 4 L25.5 7.5 L22 11" stroke="#fff" stroke-width="2" fill="none"/></svg>
  </section>

  <!-- Pie charts -->
  <section class="slide slide--light pos-d">
    <div class="slide-tag"><span class="slide-tag__label">Pie</span><span class="slide-tag__num">03</span><span class="slide-tag__rule"></span><span class="slide-tag__brand">NodeHarbor</span></div>
    <h2 class="slide-title">DATA <b>CHARTS:</b> Pie</h2>
    <p class="slide-intro">This is an example to be replace with own text here, or what you want to put a here instead this dummy text Dont forget to remove this once you put your own text.</p>

    <svg class="donut" style="left:53px;top:102px" viewBox="0 0 120 120" aria-label="Donut chart 30 and 70 percent">
      <circle cx="60" cy="60" r="39.5" fill="none" stroke="#333b43" stroke-width="37"/>
      <circle cx="60" cy="60" r="39.5" fill="none" stroke="#7c8891" stroke-width="37" stroke-dasharray="74.5 248.2" transform="rotate(-144 60 60)"/>
    </svg>
    <svg class="donut" style="left:286px;top:102px" viewBox="0 0 120 120" aria-label="Donut chart 30 and 70 percent">
      <circle cx="60" cy="60" r="39.5" fill="none" stroke="#0b6fa6" stroke-width="37"/>
      <circle cx="60" cy="60" r="39.5" fill="none" stroke="#7c8891" stroke-width="37" stroke-dasharray="74.5 248.2" transform="rotate(-144 60 60)"/>
    </svg>
    <svg class="callout-lines" viewBox="0 0 551 250" aria-hidden="true">
      <g stroke="#0b6fa6" stroke-width="1" fill="#0b6fa6">
        <line x1="153" y1="123" x2="182" y2="123"/><circle cx="153" cy="123" r="2"/>
        <line x1="170" y1="188" x2="182" y2="188"/><circle cx="170" cy="188" r="2"/>
        <line x1="378" y1="123" x2="416" y2="123"/><circle cx="378" cy="123" r="2" fill="#7c8891" stroke="#7c8891"/>
        <line x1="405" y1="188" x2="416" y2="188"/><circle cx="405" cy="188" r="2" fill="#333b43" stroke="#333b43"/>
      </g>
    </svg>
    <div class="pie-callout" style="left:185px;top:114px"><div class="pie-value">30%</div><div class="pie-heading">Sample Heading 1</div><p class="pie-body">This is an example to be replace with own text here</p></div>
    <div class="pie-callout" style="left:185px;top:180px"><div class="pie-value">70%</div><div class="pie-heading">Sample Heading 1</div><p class="pie-body">This is an example to be replace with own text here</p></div>
    <div class="pie-callout" style="left:420px;top:114px"><div class="pie-value">30%</div><div class="pie-heading">Sample Heading 1</div><p class="pie-body">This is an example to be replace with own text here</p></div>
    <div class="pie-callout" style="left:420px;top:180px"><div class="pie-value">70%</div><div class="pie-heading">Sample Heading 1</div><p class="pie-body">This is an example to be replace with own text here</p></div>

    <div class="slide-divider"></div>
    <p class="slide-footnote">This is an example to be replace with own text here, or what you want to put a here instead this dummy text. Dont forget to remove this once you put your own text.<br>This is an example to be replace with own text here, or what you want to put a here instead this dummy text.</p>
    <svg class="slide-nav" viewBox="0 0 31 15" aria-label="Previous and next"><circle cx="7.5" cy="7.5" r="7.5" fill="#0b6fa6"/><path d="M9 4 L5.5 7.5 L9 11" stroke="#fff" stroke-width="2" fill="none"/><circle cx="23.5" cy="7.5" r="7.5" fill="#0b6fa6"/><path d="M22 4 L25.5 7.5 L22 11" stroke="#fff" stroke-width="2" fill="none"/></svg>
  </section>

  <!-- Section header options -->
  <section class="slide slide--light pos-e">
    <div class="slide-tag"><span class="slide-tag__label">Options</span><span class="slide-tag__num">02</span><span class="slide-tag__rule"></span><span class="slide-tag__brand">NodeHarbor</span></div>
    <h2 class="slide-title">SECTION <b>HEADER:</b> Options</h2>
    <p class="slide-intro" style="top:75px">This is an example to be replace with own text here, or what you want to put a here instead this dummy text Dont forget to remove this once you put your own text.</p>
    <article class="option-card" style="left:50px;top:114px">
      <div class="option-visual option-visual--grey" role="img" aria-label="Portrait placeholder for team member"></div>
      <h3 class="option-heading">Sample Heading 1</h3>
      <p class="option-body">This is an example to be replace with own text here, or what you want to put a here instead this dummy text. Dont forget to remove this once you put your own text. This is an example to be replace with own text here, or what you want to put a here instead this dummy text.</p>
    </article>
    <article class="option-card" style="left:215px;top:114px">
      <div class="option-visual option-visual--blue" role="img" aria-label="Portrait placeholder for team member"></div>
      <h3 class="option-heading">Sample Heading 1</h3>
      <p class="option-body">This is an example to be replace with own text here, or what you want to put a here instead this dummy text. Dont forget to remove this once you put your own text. This is an example to be replace with own text here, or what you want to put a here instead this dummy text.</p>
    </article>
    <article class="option-card" style="left:377px;top:114px">
      <div class="option-visual option-visual--dark" role="img" aria-label="Portrait placeholder for team member"></div>
      <h3 class="option-heading">Sample Heading 1</h3>
      <p class="option-body">This is an example to be replace with own text here, or what you want to put a here instead this dummy text. Dont forget to remove this once you put your own text. This is an example to be replace with own text here, or what you want to put a here instead this dummy text.</p>
    </article>
    <svg class="slide-nav" viewBox="0 0 31 15" aria-label="Previous and next"><circle cx="7.5" cy="7.5" r="7.5" fill="#0b6fa6"/><path d="M9 4 L5.5 7.5 L9 11" stroke="#fff" stroke-width="2" fill="none"/><circle cx="23.5" cy="7.5" r="7.5" fill="#0b6fa6"/><path d="M22 4 L25.5 7.5 L22 11" stroke="#fff" stroke-width="2" fill="none"/></svg>
  </section>

  <!-- Thank you -->
  <section class="slide slide--brand pos-f">
    <svg class="closing-bubbles" viewBox="170 50 245 165" aria-label="Speech bubbles">
      <path d="M321 119 h79 a5 5 0 0 1 5 5 v36 a5 5 0 0 1 -5 5 h-10 l14 18 l-26 -18 h-57 a5 5 0 0 1 -5 -5 v-36 a5 5 0 0 1 5 -5 z" fill="#7c8891"/>
      <path d="M182 140 h81 a5 5 0 0 1 5 5 v40 a5 5 0 0 1 -5 5 h-6 l7 15 l-22 -15 h-60 a5 5 0 0 1 -5 -5 v-40 a5 5 0 0 1 5 -5 z" fill="none" stroke="#ffffff" stroke-width="1.2"/>
      <path d="M204 58 h131 a6 6 0 0 1 6 6 v60 a6 6 0 0 1 -6 6 h-98 l-34 30 l12 -30 h-11 a6 6 0 0 1 -6 -6 v-60 a6 6 0 0 1 6 -6 z" fill="#333b43"/>
      <text x="269" y="91" text-anchor="middle" font-family="Roboto Condensed, sans-serif" font-weight="700" font-size="16" fill="#ffffff" letter-spacing=".4">LETS TALK</text>
      <text x="269" y="111" text-anchor="middle" font-family="Roboto Condensed, sans-serif" font-weight="700" font-size="16" fill="#ffffff" letter-spacing=".4">NOW</text>
    </svg>
    <div class="closing-rule closing-rule--left"></div>
    <div class="closing-rule closing-rule--right"></div>
    <h2 class="closing-title">THANK YOU</h2>
    <p class="closing-note">This is an example to be replace<br>with own text here</p>
  </section>

</main>
</body>
</html>
```